Lawn Sign Design – Brisko

We need a clean, eye-catching 18" x 24" lawn sign for Brisko that effectively communicates our core message while maintaining strong brand consistency.

Key Elements to Include:
Tagline (Main Focus): Upgrade Your Roof Without Replacing It
Website: www.tryvexlo-demo.example
Phone Number: (877) BRISKO-GO
RQMH License Number: 4830516
Brisko Logo & Branding: Ensure the logo, corporate colors, and custom font are used consistently to align with our existing branding.

Design Guidelines:
Simple & High-Impact: The tagline should be the most prominent element on the sign, drawing immediate attention.
Easy Readability: Use a bold, clean design with high contrast for quick readability from a distance.
Balanced Layout: Place supporting details (website, phone number, and RQMH number) in a visually clear but secondary position to the tagline.
Professional & Modern: The sign should reflect credibility and innovation in the roofing industry.

Deliverables:
High-resolution print-ready files (CMYK)
A digital proof for review before finalizing
The final design should make a strong impression with minimal text, ensuring that anyone passing by can instantly grasp what we offer.

I am including our custom font. To get an hexagon in our name, simply type the $ after the 'O" Please use this font for anything you type.

```html
<!DOCTYPE html>
<html lang="en">
<head>
<meta charset="utf-8">
<title>Brisko Lawn Sign</title>
<link href="https://fonts.googleapis.com/css2?family=Poppins:wght@400;500;600;700;800;900&display=swap" rel="stylesheet">
<style>
  :root {
    --page-bg: #d8dadd;
    --sign-bg: #f0f1f5;
    --sign-sheen: #fafbfc;
    --brand-blue: #0f55a3;
    --ink: #39393b;
    --white: #ffffff;
  }
  html, body {
    margin: 0;
    padding: 0;
    width: 1200px;
    height: 1024px;
    overflow: hidden;
    background: var(--page-bg);
    font-family: "Poppins", sans-serif;
  }
  .lawn-sign {
    position: absolute;
    left: 40px;
    top: 92px;
    width: 1120px;
    height: 841px;
    box-shadow: 0 10px 30px rgba(0,0,0,0.18);
  }
  .lawn-sign svg { display: block; width: 100%; height: 100%; }
  .sign-face { fill: url(#sheen); }
  .frame-line { fill: none; stroke: var(--brand-blue); stroke-width: 3.5; }
  .brand-name { fill: var(--brand-blue); font-weight: 700; font-size: 100px; letter-spacing: 4px; }
  .tagline-main { fill: var(--ink); font-weight: 800; font-size: 168px; letter-spacing: -3px; }
  .tagline-sub { fill: var(--brand-blue); font-weight: 700; font-size: 84px; letter-spacing: -3px; }
  .license-pill { fill: var(--brand-blue); }
  .license-text { fill: var(--white); font-size: 36px; font-weight: 400; }
  .license-text .license-number { font-weight: 700; }
  .contact-icon { fill: var(--brand-blue); }
  .contact-icon-glyph { fill: none; stroke: var(--white); stroke-width: 2.4; stroke-linecap: round; }
  .contact-phone { fill: var(--ink); font-size: 50px; font-weight: 500; }
  .contact-web { fill: var(--ink); font-size: 40px; font-weight: 400; }
  .contact-web .web-domain { font-weight: 600; }
</style>
</head>
<body>
  <div class="lawn-sign">
    <svg viewBox="0 0 1152 865" xmlns="http://www.w3.org/2000/svg">
      <defs>
        <linearGradient id="sheen" x1="0" y1="0" x2="1" y2="1">
          <stop offset="0" stop-color="#f0f1f5"/>
          <stop offset="0.12" stop-color="#e9eaee"/>
          <stop offset="0.2" stop-color="#f1f2f6"/>
          <stop offset="0.75" stop-color="#f0f1f5"/>
          <stop offset="0.85" stop-color="#e8e9ed"/>
          <stop offset="1" stop-color="#f2f3f6"/>
        </linearGradient>
      </defs>

      <rect class="sign-face" x="0" y="0" width="1152" height="865"/>

      <path class="frame-line" d="M270,121 H78 A25,25 0 0 0 53,146 V682 A25,25 0 0 0 78,707 H260 M892,707 H1075 A25,25 0 0 0 1100,682 V146 A25,25 0 0 0 1075,121 H913"/>

      <text class="brand-name" x="591" y="166" text-anchor="middle">BRISKO</text>

      <text class="tagline-main" x="576" y="379" text-anchor="middle" textLength="780" lengthAdjust="spacingAndGlyphs">UPGRADE</text>
      <text class="tagline-main" x="576" y="529" text-anchor="middle" textLength="948" lengthAdjust="spacingAndGlyphs">YOUR ROOF</text>
      <text class="tagline-sub" x="576" y="629" text-anchor="middle" textLength="948" lengthAdjust="spacingAndGlyphs">WITHOUT REPLACING IT</text>

      <rect class="license-pill" x="257" y="678" width="638" height="52" rx="26"/>
      <text class="license-text" x="576" y="717" text-anchor="middle">RQMH License Number: <tspan class="license-number">4830516</tspan></text>

      <g class="contact-phone-group">
        <circle class="contact-icon" cx="77" cy="794" r="19"/>
        <path class="contact-icon-glyph" d="M70,784 q-3,3 0,9 q4,8 12,11 q4,1 6,-2 l-4,-4 l-3,2 q-5,-3 -7,-8 l2,-3 z"/>
        <text class="contact-phone" x="104" y="812">(877) BRISKO-GO</text>
      </g>

      <g class="contact-web-group">
        <circle class="contact-icon" cx="642" cy="794" r="19"/>
        <circle class="contact-icon-glyph" cx="642" cy="794" r="11"/>
        <path class="contact-icon-glyph" d="M631,794 H653 M642,783 q-7,11 0,22 M642,783 q7,11 0,22"/>
        <text class="contact-web" x="671" y="808" textLength="426" lengthAdjust="spacingAndGlyphs"><tspan class="web-domain">tryvexlo-demo</tspan>.example</text>
      </g>
    </svg>
  </div>
</body>
</html>
```